Real Estate Seller Financing Postcard

I need a postcard that lays out these options contained in the notes that grabs attention, explains the two options easily and is eye-catching. The front needs to have the percentages on it and information about it and on the other side One side exact Text is:
"Monthly income without tenant headaches" in big letters. Also on front "Get
110%
add an "or"
160% of market value for your property. ". The percentages should be displayed and that is not to be a sentence of text. Other side text: I need bullets points for these "Formal protection as a lien holder against home
No commission or closing cost
Fast closings possible
Property taken as is so no repairs.

Add to the top of the back in "It’s simple. I am a new investor without down payment capital who still want to double our portfolio this year to grow our portfolio."
Here are the two options that are to be the largest part of the back
Option 1, you can receive 80% now cash and 30% over a short period of time including interest.

Option 2, where act like a bank allowing you to make 150% if you finance the whole property(ies). No gimmicks and surprises, just simple unconventional financing.

Include Logo Somewhere

Target Market(s)

Property Owners Wanting to Sell Their Property

Industry/Entity Type

Real Estate Investing

Requirements
Must have
• The options promiment and each side with its respective information. Must have logo somewhere
Nice to have
• The options in color other than black.
Should not have
• A picture of money on the front. Any other image is okay.

```html
<!DOCTYPE html>
<html lang="en">
<head>
<meta charset="utf-8">
<title>Meridian Real Estate Group – Seller Financing Postcard</title>
<link rel="stylesheet" href="https://fonts.googleapis.com/css2?family=Montserrat:wght@400;500;600;700;800&display=swap">
<style>
  :root {
    --brand-blue: #0b3f9b;
    --brand-blue-deep: #06307d;
    --ink: #1c1c28;
    --ink-soft: #3a3a46;
    --paper: #ffffff;
    --panel-light: #dbe8f7;
    --panel-pale: #f3f7fd;
    --photo-top: #8fb6dc;
    --photo-bottom: #3f6fa6;
    --page-bg: #e4e4e4;
  }
  * { margin: 0; padding: 0; box-sizing: border-box; }
  html, body {
    width: 1200px;
    height: 2328px;
    overflow: hidden;
    background: var(--page-bg);
    font-family: "Montserrat", Arial, sans-serif;
  }
  .sheet {
    position: relative;
    width: 1200px;
    height: 2328px;
  }
  .postcard {
    position: absolute;
    left: 80px;
    width: 1040px;
    height: 742px;
    background: var(--paper);
    box-shadow: 0 10px 28px rgba(0,0,0,0.22);
    overflow: hidden;
  }
  .postcard--front { top: 382px; }
  .postcard--back { top: 1204px; }
  .postcard svg { display: block; width: 100%; height: 100%; }

  .fill-blue { fill: var(--brand-blue); }
  .fill-deep { fill: var(--brand-blue-deep); }
  .fill-white { fill: var(--paper); }

  .t { font-family: "Montserrat", Arial, sans-serif; }
  .brand-name { font-weight: 700; fill: var(--brand-blue); }
  .headline-band { font-weight: 800; fill: var(--paper); font-size: 66px; letter-spacing: 1px; }
  .headline { font-weight: 800; fill: var(--brand-blue); font-size: 40px; }
  .get-label { font-weight: 800; fill: var(--ink); font-size: 34px; letter-spacing: 1px; }
  .percent { font-weight: 700; fill: var(--paper); font-size: 33px; letter-spacing: 1px; }
  .market-note { font-weight: 700; fill: var(--ink); font-size: 17.5px; letter-spacing: 0.6px; }
  .tab-label { font-weight: 700; fill: var(--paper); font-size: 20px; letter-spacing: 0.5px; }
  .contact-phone { font-weight: 700; fill: var(--ink); font-size: 19px; letter-spacing: 0.6px; }
  .contact-line { font-weight: 500; fill: var(--ink); font-size: 16px; letter-spacing: 0.5px; }
  .contact-line .accent { font-weight: 700; fill: var(--brand-blue); }
  .lead-title { font-weight: 700; fill: var(--brand-blue); font-size: 21px; letter-spacing: 0.4px; }
  .body-copy { font-weight: 500; fill: var(--ink-soft); font-size: 14.5px; letter-spacing: 0.4px; }
  .body-copy .accent { font-weight: 700; fill: var(--brand-blue); }
  .protection-title { font-weight: 700; fill: var(--brand-blue); font-size: 20.5px; letter-spacing: 0.5px; }
  .bullet-text { font-weight: 600; fill: var(--ink); font-size: 15.5px; letter-spacing: 0.5px; }
  .icon-stroke { fill: none; stroke: var(--paper); stroke-width: 1.6; stroke-linecap: round; stroke-linejoin: round; }
  .address-line { stroke: #777; stroke-width: 1.2; }
  .stamp-box { fill: none; stroke: #555; stroke-width: 1.5; }
  .brand-ring { fill: none; stroke: var(--brand-blue); stroke-width: 3; }
  .brand-divider { stroke: #777; stroke-width: 1.5; }
</style>
</head>
<body>
<main class="sheet">

  <!-- Front side -->
  <section class="postcard postcard--front" aria-label="Postcard front">
    <svg viewBox="0 0 978 698" xmlns="http://www.w3.org/2000/svg">
      <defs>
        <linearGradient id="frontPanel" x1="0" y1="0" x2="1" y2="0">
          <stop offset="0" stop-color="#ffffff"/>
          <stop offset="1" stop-color="#e3edf9"/>
        </linearGradient>
        <linearGradient id="photoTone" x1="0" y1="0" x2="0.3" y2="1">
          <stop offset="0" stop-color="var(--photo-top)"/>
          <stop offset="0.55" stop-color="#6e97c6"/>
          <stop offset="1" stop-color="var(--photo-bottom)"/>
        </linearGradient>
      </defs>

      <rect class="front-panel" x="0" y="0" width="978" height="698" fill="url(#frontPanel)"/>

      <!-- Photo area -->
      <polygon class="hero-photo" role="img" aria-label="Photo of a businessman holding a glowing model of city towers in his open palm"
               points="420,0 978,0 978,698 560,698 630,420" fill="url(#photoTone)"/>

      <!-- Diagonal accents -->
      <polygon class="fill-blue" points="368,0 432,0 632,420 606,430"/>
      <polygon class="fill-deep" points="846,0 978,0 905,112"/>
      <polygon class="fill-blue" points="846,112 878,62 905,112"/>
      <polygon class="fill-deep" points="490,482 546,482 454,698 430,698"/>
      <polygon class="fill-white" points="552,482 566,482 476,698 462,698"/>
      <polygon class="fill-blue" points="601,486 728,698 476,698"/>

      <!-- Brand -->
      <circle class="brand-ring" cx="84" cy="85" r="48"/>
      <line class="brand-divider" x1="150" y1="48" x2="150" y2="122"/>
      <text class="t brand-name" x="168" y="90" font-size="40">MERIDIAN</text>
      <text class="t brand-name" x="169" y="116" font-size="16.5">REAL ESTATE GROUP</text>

      <!-- Headline -->
      <polygon class="fill-blue" points="35,171 440,171 452,181 472,244 35,244"/>
      <polygon class="fill-deep" points="440,171 460,171 472,244 452,181"/>
      <text class="t headline-band" x="46" y="233">MONTHLY</text>
      <text class="t headline" x="35" y="293">INCOME WITHOUT</text>
      <text class="t headline" x="35" y="340">TENANT HEADACHES</text>

      <!-- Percentages -->
      <text class="t get-label" x="35" y="394">GET</text>
      <rect class="fill-blue" x="128" y="381" width="383" height="7"/>

      <polygon class="fill-blue" points="35,408 170,408 184,454 35,454"/>
      <polygon class="fill-deep" points="170,408 178,408 192,454 184,454"/>
      <text class="t percent" x="48" y="443">100%</text>

      <polygon class="fill-blue" points="196,408 331,408 345,454 196,454"/>
      <polygon class="fill-deep" points="331,408 339,408 353,454 345,454"/>
      <text class="t percent" x="210" y="443">110%</text>

      <polygon class="fill-blue" points="357,408 492,408 506,454 357,454"/>
      <polygon class="fill-deep" points="492,408 500,408 514,454 506,454"/>
      <text class="t percent" x="370" y="443">160%</text>

      <text class="t market-note" x="35" y="481">OF MARKET VALUE FOR YOUR PROPERTY.</text>

      <!-- Contact -->
      <polygon class="fill-blue" points="35,511 185,511 196,543 35,543"/>
      <text class="t tab-label" x="49" y="534">Contact Us</text>
      <rect class="fill-blue" x="200" y="534" width="306" height="6"/>

      <g class="contact-row">
        <polygon class="fill-blue" points="35,554 84,554 92,585 35,585"/>
        <path class="icon-stroke" d="M53,561 l4,0 l2,6 l-3,2 a14,14 0 0 0 7,7 l2,-3 l6,2 l0,4 a3,3 0 0 1 -3,3 a20,20 0 0 1 -18,-18 a3,3 0 0 1 3,-3 z"/>
        <text class="t contact-phone" x="96" y="577">5550142876 \ 5550193412</text>
      </g>
      <g class="contact-row">
        <polygon class="fill-blue" points="35,593 84,593 92,624 35,624"/>
        <rect class="icon-stroke" x="51" y="602" width="20" height="14"/>
        <path class="icon-stroke" d="M51,602 l10,8 l10,-8"/>
        <text class="t contact-line" x="96" y="614">info@<tspan class="accent">meridianestategroup</tspan>.com</text>
      </g>
      <g class="contact-row">
        <polygon class="fill-blue" points="35,632 84,632 92,663 35,663"/>
        <circle class="icon-stroke" cx="61" cy="647" r="9"/>
        <ellipse class="icon-stroke" cx="61" cy="647" rx="4" ry="9"/>
        <path class="icon-stroke" d="M52,647 h18 M54,642 h14 M54,652 h14"/>
        <text class="t contact-line" x="96" y="653">www.<tspan class="accent">meridianestategroup</tspan>.com</text>
      </g>
    </svg>
  </section>

  <!-- Back side -->
  <section class="postcard postcard--back" aria-label="Postcard back">
    <svg viewBox="0 0 978 698" xmlns="http://www.w3.org/2000/svg">
      <defs>
        <linearGradient id="backPanel" x1="0" y1="0" x2="0.6" y2="1">
          <stop offset="0" stop-color="var(--panel-light)"/>
          <stop offset="1" stop-color="var(--panel-pale)"/>
        </linearGradient>
      </defs>

      <rect x="0" y="0" width="978" height="698" fill="var(--paper)"/>
      <polygon class="info-panel" points="0,0 300,0 612,545 560,698 0,698" fill="url(#backPanel)"/>

      <!-- Diagonal accents -->
      <polygon class="fill-blue" points="290,0 346,0 616,540 596,548"/>
      <polygon class="fill-deep" points="360,0 382,0 626,500 612,508"/>
      <polygon class="fill-deep" points="388,0 478,0 438,98"/>
      <polygon class="fill-blue" points="616,540 612,698 566,698"/>
      <polygon class="fill-deep" points="488,559 588,698 396,698"/>

      <!-- Intro -->
      <text class="t lead-title" x="35" y="49">It’s simple.</text>
      <text class="t body-copy" x="35" y="71">I am a new investor without down</text>
      <text class="t body-copy" x="35" y="87">payment capital who still want to</text>
      <text class="t body-copy" x="35" y="103">double our portfolio this year to grow</text>
      <text class="t body-copy" x="35" y="119">our portfolio.</text>

      <!-- Option 1 -->
      <polygon class="fill-blue" points="35,143 155,143 166,174 35,174"/>
      <text class="t tab-label" x="49" y="166">Option 1</text>
      <text class="t body-copy" x="35" y="193">you can receive <tspan class="accent">80%</tspan> now cash and <tspan class="accent">30%</tspan> over</text>
      <text class="t body-copy" x="35" y="212">a short period of time including interest.</text>

      <!-- Option 2 -->
      <polygon class="fill-blue" points="35,233 155,233 166,264 35,264"/>
      <text class="t tab-label" x="49" y="256">Option 2</text>
      <text class="t body-copy" x="35" y="283">where act like a bank allowing you to make <tspan class="accent">150%</tspan></text>
      <text class="t body-copy" x="35" y="302">if you finance the whole property(ies). No gimmicks</text>
      <text class="t body-copy" x="35" y="321">and surprises, just simple unconventional financing.</text>

      <rect class="fill-blue" x="35" y="336" width="423" height="5"/>

      <!-- Protection -->
      <text class="t protection-title" x="34" y="370">Formal protection as a lien holder</text>
      <text class="t protection-title" x="34" y="393">against home</text>
      <circle class="fill-blue" cx="40" cy="421" r="4"/>
      <text class="t bullet-text" x="50" y="427">No commission or closing cost</text>
      <circle class="fill-blue" cx="40" cy="448" r="4"/>
      <text class="t bullet-text" x="50" y="454">Fast closings possible</text>
      <circle class="fill-blue" cx="40" cy="475" r="4"/>
      <text class="t bullet-text" x="50" y="481">Property taken as is so no repairs.</text>

      <!-- Contact -->
      <polygon class="fill-blue" points="35,512 185,512 196,543 35,543"/>
      <text class="t tab-label" x="49" y="535">Contact Us</text>
      <rect class="fill-blue" x="200" y="534" width="272" height="6"/>

      <g class="contact-row">
        <polygon class="fill-blue" points="35,554 84,554 92,585 35,585"/>
        <path class="icon-stroke" d="M53,561 l4,0 l2,6 l-3,2 a14,14 0 0 0 7,7 l2,-3 l6,2 l0,4 a3,3 0 0 1 -3,3 a20,20 0 0 1 -18,-18 a3,3 0 0 1 3,-3 z"/>
        <text class="t contact-phone" x="96" y="577">5550142876 \ 5550193412</text>
      </g>
      <g class="contact-row">
        <polygon class="fill-blue" points="35,593 84,593 92,624 35,624"/>
        <rect class="icon-stroke" x="51" y="602" width="20" height="14"/>
        <path class="icon-stroke" d="M51,602 l10,8 l10,-8"/>
        <text class="t contact-line" x="96" y="614">info@<tspan class="accent">meridianestategroup</tspan>.com</text>
      </g>
      <g class="contact-row">
        <polygon class="fill-blue" points="35,632 84,632 92,663 35,663"/>
        <circle class="icon-stroke" cx="61" cy="647" r="9"/>
        <ellipse class="icon-stroke" cx="61" cy="647" rx="4" ry="9"/>
        <path class="icon-stroke" d="M52,647 h18 M54,642 h14 M54,652 h14"/>
        <text class="t contact-line" x="96" y="653">www.<tspan class="accent">meridianestategroup</tspan>.com</text>
      </g>

      <!-- Mailing side -->
      <circle class="brand-ring" cx="543" cy="104" r="36"/>
      <line class="brand-divider" x1="593" y1="74" x2="593" y2="132"/>
      <text class="t brand-name" x="606" y="112" font-size="30">MERIDIAN</text>
      <text class="t brand-name" x="607" y="130" font-size="12.5">REAL ESTATE GROUP</text>

      <rect class="stamp-box" x="804" y="35" width="139" height="139"/>

      <line class="address-line" x1="507" y1="270" x2="943" y2="270"/>
      <line class="address-line" x1="552" y1="349" x2="943" y2="349"/>
      <line class="address-line" x1="597" y1="428" x2="943" y2="428"/>
    </svg>
  </section>

</main>
</body>
</html>
```